Sudsy Harbor Laundromat Wordpress Design

We need a Wordpress website design for our laundromat, Sudsy Harbor Atlanta, at www.sudsyharborlaunder.example. We would like to have 6 pages: Home, About Us, Services, Locations, Reviews and Contact us. We will provide content for the text on each page. What we do: We are a full service laundromat that provides dry cleaning drop off, professional laundry services, wash dry fold and self service laundry to the local community. We would like to use the color scheme from our logo to convey a warm, safe, and bright business that caters to its diverse community.
Updates

I like the structure of this laundromat website: http://www.tumblewashexample.com/ Using my logo and color scheme in the above referenced website is what. Am looking for. The photos attached to the project with the female model should be used as a primary focus and supplemented by actual photos of the equipment.

Target Market(s)

Our target market is a diverse group of people from the neighborhood - LGBTQ community /Locals/Regulars that have been coming to laundromat for 30 years.

Industry/Entity Type

Laundromat

Coding

Coded - Design and coding required

Number of Pages Required

5+ page

Font styles to use
Sans Serif

Colors
0054AA
0677BA
7BADD7
CADEEF
E8F1F8

Requirements
Must have
• Feature this video on the main page: https://videos.example.net/wq7PzrT2kLm

```html
<!DOCTYPE html>
<html lang="en">
<head>
<meta charset="utf-8">
<title>Sudsy Harbor Laundromat</title>
<link rel="stylesheet" href="https://fonts.googleapis.com/css2?family=Oswald:wght@300;400;500&family=Poppins:wght@300;400;500&family=Roboto+Slab:wght@800&display=swap">
<style>
:root{
  --primary:#0054AA;
  --mid:#0677BA;
  --soft:#7BADD7;
  --pale:#CADEEF;
  --mist:#E8F1F8;
  --bright:#17A2E6;
  --navy:#0A1F48;
  --ink:#3a3f4a;
  --heading:#1460B8;
}
*{margin:0;padding:0;box-sizing:border-box}
html,body{width:1200px;height:3626px;overflow:hidden}
body{position:relative;background:#fff;font-family:'Poppins',sans-serif;color:var(--ink)}
.abs{position:absolute}
.btn{position:absolute;display:flex;align-items:center;justify-content:center;background:var(--bright);color:#fff;font-family:'Oswald',sans-serif;font-size:15px;border-radius:6px;text-transform:uppercase}

.topbar{left:0;top:0;width:1200px;height:33px;background:var(--primary);color:#fff}
.topbar .hours{left:776px;top:8px;font-size:12px}
.topbar .phone{left:1034px;top:3px;font-family:'Oswald',sans-serif;font-size:19px}

.nav{left:0;top:33px;width:1200px;height:71px;background:#fff}
.brand{display:flex;align-items:center;gap:8px}
.brand .dot{width:14px;height:14px;border-radius:50%;background:var(--bright)}
.brand .name{font-family:'Oswald',sans-serif;font-weight:500;color:var(--primary);font-size:26px;letter-spacing:.5px}
.nav .brand{left:59px;top:18px}
.menu{left:702px;top:28px;display:flex;gap:20px;font-size:12px;color:#333}
.menu .active{color:var(--bright);position:relative}
.menu .active::after{content:"";position:absolute;left:50%;top:22px;width:4px;height:4px;margin-left:-2px;border-radius:50%;background:var(--bright)}

.hero{left:0;top:104px;width:1200px;height:607px;background:linear-gradient(135deg,#9fb8c2 0%,#7f9aa6 45%,#5f7a88 100%)}
.hero-circle{left:78px;top:134px;width:416px;height:416px;border-radius:50%;background:rgba(255,255,255,.9)}
.hero-title{left:78px;top:188px;width:416px;text-align:center;font-family:'Roboto Slab',serif;font-weight:800;font-size:54px;line-height:57px;color:#103f85}
.hero-title .accent{color:var(--bright)}
.hero-text{left:130px;top:368px;width:312px;text-align:center;font-size:12px;line-height:21px;color:#333}
.slider-nav{display:flex;align-items:center;gap:14px}
.slider-nav .line{width:84px;height:1px;background:var(--mid)}
.arrow{width:40px;height:40px;border-radius:50%;display:flex;align-items:center;justify-content:center}
.arrow.fill{background:var(--bright)}
.arrow.ring{border:1.5px solid var(--primary)}

.welcome{left:0;top:711px;width:1200px;height:496px;background:var(--mist)}
.label{font-size:14px;color:#444}
.sec-title{font-family:'Oswald',sans-serif;font-weight:400;color:var(--heading);text-transform:uppercase}
.para{font-size:12px;line-height:21px;color:#555}
.feature{position:absolute;width:140px;text-align:center;font-family:'Oswald',sans-serif;font-weight:300;font-size:15px;line-height:21px;color:#222}
.feature svg{display:block;margin:0 auto 8px}

.card{position:absolute;width:338px;height:218px;background:#fff;border-radius:26px;box-shadow:-4px 4px 10px rgba(0,60,130,.09)}
.card svg{position:absolute;left:28px;top:20px}
.card h3{position:absolute;left:28px;top:92px;font-family:'Oswald',sans-serif;font-weight:400;font-size:18px;color:var(--heading);text-transform:uppercase}
.card p{position:absolute;left:29px;top:126px;width:290px;font-size:11.5px;line-height:20px;color:#555}

.benefits{left:0;top:1687px;width:1200px;height:1013px;background:linear-gradient(160deg,#0a5cb6 0%,var(--primary) 55%,#0a4fa0 100%)}
.video-shadow{left:614px;top:1790px;width:360px;height:258px;background:#0a3d84;border-radius:6px}
.video{left:629px;top:1770px;width:412px;height:262px;border-radius:6px;background:linear-gradient(135deg,#c9c3bb,#8f8a86 55%,#6d6c70)}
.play{left:808px;top:1876px;width:54px;height:48px}
.map-shadow{left:145px;top:2274px;width:338px;height:222px;background:#0a3d84}
.map{left:159px;top:2254px;width:383px;height:224px;background:linear-gradient(135deg,#eef1f4,#e2e8ee)}
.areas{left:670px;top:2146px;width:359px;height:346px;border:1px dashed rgba(160,200,240,.5);border-radius:6px}
.area{position:absolute;left:28px;width:305px;display:flex;align-items:center;gap:12px;font-family:'Oswald',sans-serif;font-size:14px;color:#fff}
.area .chev{margin-left:auto}
.area-sep{position:absolute;left:24px;width:312px;height:1px;background:rgba(160,200,240,.25)}

.testi{position:absolute;width:260px;text-align:center}
.avatar{position:relative;width:82px;height:82px;margin:0 auto;border-radius:50%;background:radial-gradient(circle at 50% 45%,#d9a27a,#7a4a30)}
.avatar .q{position:absolute;right:-14px;top:-2px;width:28px;height:28px;border-radius:50%;background:var(--bright);color:#fff;font-family:'Oswald',sans-serif;font-size:24px;line-height:34px;text-align:center}
.testi p{margin-top:22px;font-size:12px;line-height:20px;color:#555}
.testi .who{margin-top:16px;font-family:'Oswald',sans-serif;font-size:14px;color:var(--bright)}

.footer{left:0;top:3160px;width:1200px;height:423px;background:var(--navy)}
.cta-text{left:289px;top:3218px;font-family:'Oswald',sans-serif;font-size:27px;line-height:34px;color:#fff}
.rule{left:60px;top:3323px;width:1080px;height:1px;background:rgba(255,255,255,.12)}
.col-title{font-family:'Oswald',sans-serif;font-size:15px;color:var(--bright);text-transform:uppercase}
.links{list-style:none;font-size:11.5px;color:#fff}
.links li{height:24px;position:relative;padding-left:20px}
.links li::before{content:"";position:absolute;left:0;top:6px;width:5px;height:5px;border-radius:50%;background:var(--bright)}
.social{position:absolute;width:42px;height:42px;border-radius:50%;border:2px solid #fff;background:var(--primary)}
.icon-badge{position:absolute;width:38px;height:38px;border-radius:50%;background:var(--bright);display:flex;align-items:center;justify-content:center}
.copyright{left:0;top:3583px;width:1200px;height:43px;background:var(--bright);color:#fff;font-size:11px;text-align:center;line-height:43px}
</style>
</head>
<body>

<div class="abs topbar">
  <svg class="abs" style="left:754px;top:8px" width="17" height="17" viewBox="0 0 17 17"><circle cx="8.5" cy="8.5" r="7" fill="none" stroke="#5fc3f5" stroke-width="1.5"/><path d="M8.5 4.5v4.2l2.8 1.8" fill="none" stroke="#5fc3f5" stroke-width="1.5"/></svg>
  <div class="abs hours">Open : Every Day 7am to 9pm</div>
  <svg class="abs" style="left:1006px;top:7px" width="19" height="19" viewBox="0 0 24 24"><path d="M6.6 10.8a15 15 0 0 0 6.6 6.6l2.2-2.2a1 1 0 0 1 1-.25 11.4 11.4 0 0 0 3.6.57 1 1 0 0 1 1 1V20a1 1 0 0 1-1 1A17 17 0 0 1 3 4a1 1 0 0 1 1-1h3.5a1 1 0 0 1 1 1c0 1.25.2 2.45.57 3.57a1 1 0 0 1-.25 1z" fill="#5fc3f5"/></svg>
  <div class="abs phone">(404) 555 - 0182</div>
</div>

<header class="abs nav">
  <div class="abs brand"><span class="dot"></span><span class="name">SUDSY HARBOR</span></div>
  <nav class="abs menu">
    <span class="active">Home</span><span>About Us</span><span>Services</span><span>Locations</span><span>Reviews</span>
  </nav>
  <div class="btn" style="left:1035px;top:19px;width:104px;height:41px">Contact Us</div>
</header>

<section class="abs hero" role="img" aria-label="Photo of a woman in a blue dress standing beside a row of front-loading washers in the laundromat"></section>
<div class="abs hero-circle"></div>
<h1 class="abs hero-title">THE<br><span class="accent">SUDSY</span><br>HARBOR</h1>
<p class="abs hero-text">We Are A Full Service Laundromat That Provides Dry Cleaning Drop Off, Professional Laundry Services, Wash Dry Fold And Self Service Laundry To The Local Community</p>
<div class="btn" style="left:231px;top:466px;width:105px;height:40px">Contact Us</div>
<svg class="abs" style="left:0;top:560px" width="1200" height="152" viewBox="0 560 1200 152">
  <path d="M0 700 C150 650 400 590 620 600 C820 610 950 690 1200 650 L1200 712 L0 712 Z" fill="#E8F1F8"/>
</svg>
<div class="abs slider-nav" style="left:232px;top:632px">
  <span class="line"></span>
  <span class="arrow fill"><svg width="12" height="14" viewBox="0 0 12 14"><path d="M8 2 3 7l5 5" fill="none" stroke="#fff" stroke-width="2"/></svg></span>
  <span class="arrow ring"><svg width="12" height="14" viewBox="0 0 12 14"><path d="M4 2l5 5-5 5" fill="none" stroke="#0054AA" stroke-width="2"/></svg></span>
</div>

<section class="abs welcome">
  <div class="abs" role="img" aria-label="Photo of a smiling attendant holding a stack of folded towels, tinted blue" style="left:255px;top:77px;width:338px;height:214px;border-radius:4px;background:linear-gradient(135deg,#4fb4e6,#1a8fcf 60%,#137bbb)"></div>
  <div class="abs" role="img" aria-label="Photo of a woman in a blue dress seated in front of washers" style="left:184px;top:24px;width:181px;height:187px;border-radius:10px;background:linear-gradient(160deg,#d7d9da,#a8b3b9)"></div>
  <div class="abs label" style="left:676px;top:51px">Welcome To</div>
  <h2 class="abs sec-title" style="left:676px;top:76px;font-size:32px;color:var(--primary)">THE SUDSY HARBOR</h2>
  <p class="abs para" style="left:676px;top:128px;width:370px">Lorem Ipsum has been the industry's standard dummy text ever since thes, when an unknown printer took a galley of type and scrambled it to make a type specimen book. Lorem Ipsum has been the industry's standard dummy text ever since thes, when an unknown printer took.</p>
  <div class="btn" style="left:676px;top:260px;width:103px;height:39px">Learn More</div>

  <div class="feature" style="left:67px;top:355px"><svg width="28" height="28" viewBox="0 0 28 28"><path d="M6 4c5 3 8 9 8 20M22 4c-5 5-8 11-8 20" fill="none" stroke="#17A2E6" stroke-width="3" stroke-linecap="round"/><path d="M13 4c1 4 1 8 1 12" stroke="#0054AA" stroke-width="2.5" stroke-linecap="round"/></svg>Family Owned &amp; Operated</div>
  <div class="feature" style="left:221px;top:355px"><svg width="28" height="28" viewBox="0 0 28 28"><path d="M6 4c5 3 8 9 8 20M22 4c-5 5-8 11-8 20" fill="none" stroke="#17A2E6" stroke-width="3" stroke-linecap="round"/><path d="M13 4c1 4 1 8 1 12" stroke="#0054AA" stroke-width="2.5" stroke-linecap="round"/></svg>Friendly Attendants Always On Site</div>
  <div class="feature" style="left:375px;top:355px"><svg width="28" height="28" viewBox="0 0 28 28"><path d="M6 4c5 3 8 9 8 20M22 4c-5 5-8 11-8 20" fill="none" stroke="#17A2E6" stroke-width="3" stroke-linecap="round"/><path d="M13 4c1 4 1 8 1 12" stroke="#0054AA" stroke-width="2.5" stroke-linecap="round"/></svg>Your Neighborhood Spot for Fresh Laundry</div>
  <div class="feature" style="left:530px;top:355px"><svg width="28" height="28" viewBox="0 0 28 28"><path d="M6 4c5 3 8 9 8 20M22 4c-5 5-8 11-8 20" fill="none" stroke="#17A2E6" stroke-width="3" stroke-linecap="round"/><path d="M13 4c1 4 1 8 1 12" stroke="#0054AA" stroke-width="2.5" stroke-linecap="round"/></svg>The best Wash-Dry-Fold in town</div>
  <div class="feature" style="left:683px;top:355px"><svg width="28" height="28" viewBox="0 0 28 28"><path d="M6 4c5 3 8 9 8 20M22 4c-5 5-8 11-8 20" fill="none" stroke="#17A2E6" stroke-width="3" stroke-linecap="round"/><path d="M13 4c1 4 1 8 1 12" stroke="#0054AA" stroke-width="2.5" stroke-linecap="round"/></svg>Cool - Comfortable - Clean</div>
  <div class="feature" style="left:837px;top:355px"><svg width="28" height="28" viewBox="0 0 28 28"><path d="M6 4c5 3 8 9 8 20M22 4c-5 5-8 11-8 20" fill="none" stroke="#17A2E6" stroke-width="3" stroke-linecap="round"/><path d="M13 4c1 4 1 8 1 12" stroke="#0054AA" stroke-width="2.5" stroke-linecap="round"/></svg>Rows of well maintained machines</div>
  <div class="feature" style="left:990px;top:355px"><svg width="28" height="28" viewBox="0 0 28 28"><path d="M6 4c5 3 8 9 8 20M22 4c-5 5-8 11-8 20" fill="none" stroke="#17A2E6" stroke-width="3" stroke-linecap="round"/><path d="M13 4c1 4 1 8 1 12" stroke="#0054AA" stroke-width="2.5" stroke-linecap="round"/></svg>Commercial Accounts</div>
</section>

<h2 class="abs sec-title" style="left:130px;top:1273px;font-size:33px;color:var(--primary)">Services We Provide</h2>
<p class="abs para" style="left:130px;top:1321px">Fresh, Friendly &amp; Dependable Laundry Care For Our Neighbors.</p>
<div class="abs slider-nav" style="left:918px;top:1281px">
  <span class="line"></span>
  <span class="arrow fill"><svg width="12" height="14" viewBox="0 0 12 14"><path d="M8 2 3 7l5 5" fill="none" stroke="#fff" stroke-width="2"/></svg></span>
  <span class="arrow ring"><svg width="12" height="14" viewBox="0 0 12 14"><path d="M4 2l5 5-5 5" fill="none" stroke="#0054AA" stroke-width="2"/></svg></span>
</div>

<div class="card" style="left:127px;top:1394px">
  <svg width="48" height="52" viewBox="0 0 48 52"><path d="M10 6h28l8 10-8 4v28H10V20l-8-4z" fill="none" stroke="#17A2E6" stroke-width="2"/><path d="M18 6l6 8 6-8M24 14v34M10 20h28" fill="none" stroke="#17A2E6" stroke-width="2"/><rect x="20" y="1" width="8" height="5" fill="none" stroke="#17A2E6" stroke-width="2"/></svg>
  <h3>Dry Cleaning Drop Off</h3>
  <p>Lorem Ipsum has been the industry's standard dummy text ever since thes, when an unknown printer took a galley and scrambled.</p>
</div>
<div class="card" style="left:503px;top:1394px">
  <svg width="48" height="52" viewBox="0 0 48 52"><rect x="4" y="2" width="40" height="48" rx="3" fill="none" stroke="#17A2E6" stroke-width="2"/><path d="M4 12h40" stroke="#17A2E6" stroke-width="2"/><circle cx="24" cy="31" r="12" fill="none" stroke="#17A2E6" stroke-width="2"/><circle cx="24" cy="31" r="7" fill="none" stroke="#17A2E6" stroke-width="2"/><circle cx="10" cy="7" r="1.5" fill="#17A2E6"/><circle cx="16" cy="7" r="1.5" fill="#17A2E6"/></svg>
  <h3>Professional Laundry</h3>
  <p>Lorem Ipsum has been the industry's standard dummy text ever since thes, when an unknown printer took a galley and scrambled.</p>
</div>
<div class="card" style="left:869px;top:1394px">
  <svg width="58" height="52" viewBox="0 0 58 52"><path d="M14 4h30l10 12-8 4v28H12V20l-8-4z" fill="none" stroke="#17A2E6" stroke-width="2"/><path d="M22 4l7 9 7-9M29 13v35" fill="none" stroke="#17A2E6" stroke-width="2"/><path d="M4 30h50M4 38h50" stroke="#17A2E6" stroke-width="2"/></svg>
  <h3>Wash Dry Fold</h3>
  <p>Lorem Ipsum has been the industry's standard dummy text ever since thes, when an unknown printer took a galley and scrambled.</p>
</div>

<section class="abs benefits"></section>
<div class="abs" style="left:139px;top:1806px;font-size:13px;color:#3fb3f2">Why Choose Us</div>
<h2 class="abs sec-title" style="left:137px;top:1828px;font-size:33px;color:#fff">Our Laundry Benefits</h2>
<p class="abs" style="left:137px;top:1880px;width:370px;font-size:13.5px;line-height:24px;color:#fff">We Are A Full Service Laundromat That Provides Dry Cleaning Drop Off, Professional Laundry Services, Wash Dry Fold And Self Service Laundry To The Local Community</p>
<div class="btn" style="left:137px;top:1988px;width:104px;height:40px">Contact Us</div>

<div class="abs video-shadow"></div>
<div class="abs video" role="img" aria-label="Featured video still: customer in a knit hat listening to headphones inside the laundromat"></div>
<svg class="abs play" viewBox="0 0 54 48"><circle cx="27" cy="24" r="24" fill="#fff"/><path d="M21 14l16 10-16 10z" fill="#0054AA"/></svg>

<h2 class="abs" style="left:137px;top:2134px;font-family:'Oswald',sans-serif;font-weight:400;font-size:32px;color:#fff">Service Areas</h2>
<p class="abs" style="left:137px;top:2188px;width:360px;font-size:11.5px;line-height:20px;color:#fff">Lorem Ipsum has been the industry's standard dummy text ever since thes, when an unknown printer.</p>
<div class="abs map-shadow"></div>
<div class="abs map" role="img" aria-label="Street map of the neighborhood service area with nearby businesses"></div>

<div class="abs areas">
  <div class="area" style="top:16px"><svg width="14" height="18" viewBox="0 0 14 18"><path d="M7 1a6 6 0 0 0-6 6c0 4.5 6 10 6 10s6-5.5 6-10a6 6 0 0 0-6-6z" fill="none" stroke="#3fb3f2" stroke-width="1.6"/><circle cx="7" cy="7" r="2" fill="#3fb3f2"/></svg>Area Name<svg class="chev" width="8" height="12" viewBox="0 0 8 12"><path d="M2 2l4 4-4 4" fill="none" stroke="rgba(160,200,240,.6)" stroke-width="1.4"/></svg></div>
  <div class="area-sep" style="top:52px"></div>
  <div class="area" style="top:72px"><svg width="14" height="18" viewBox="0 0 14 18"><path d="M7 1a6 6 0 0 0-6 6c0 4.5 6 10 6 10s6-5.5 6-10a6 6 0 0 0-6-6z" fill="none" stroke="#3fb3f2" stroke-width="1.6"/><circle cx="7" cy="7" r="2" fill="#3fb3f2"/></svg>Area Name<svg class="chev" width="12" height="8" viewBox="0 0 12 8"><path d="M2 2l4 4 4-4" fill="none" stroke="rgba(160,200,240,.6)" stroke-width="1.4"/></svg></div>
  <p class="abs" style="left:56px;top:102px;width:240px;font-size:11px;line-height:19px;color:#fff">Lorem Ipsum has been the industry's standard dummy text ever.</p>
  <div class="area-sep" style="top:150px"></div>
  <div class="area" style="top:168px"><svg width="14" height="18" viewBox="0 0 14 18"><path d="M7 1a6 6 0 0 0-6 6c0 4.5 6 10 6 10s6-5.5 6-10a6 6 0 0 0-6-6z" fill="none" stroke="#3fb3f2" stroke-width="1.6"/><circle cx="7" cy="7" r="2" fill="#3fb3f2"/></svg>Area Name<svg class="chev" width="8" height="12" viewBox="0 0 8 12"><path d="M2 2l4 4-4 4" fill="none" stroke="rgba(160,200,240,.6)" stroke-width="1.4"/></svg></div>
  <div class="area-sep" style="top:196px"></div>
  <div class="area" style="top:213px"><svg width="14" height="18" viewBox="0 0 14 18"><path d="M7 1a6 6 0 0 0-6 6c0 4.5 6 10 6 10s6-5.5 6-10a6 6 0 0 0-6-6z" fill="none" stroke="#3fb3f2" stroke-width="1.6"/><circle cx="7" cy="7" r="2" fill="#3fb3f2"/></svg>Area Name<svg class="chev" width="8" height="12" viewBox="0 0 8 12"><path d="M2 2l4 4-4 4" fill="none" stroke="rgba(160,200,240,.6)" stroke-width="1.4"/></svg></div>
  <div class="area-sep" style="top:241px"></div>
  <div class="area" style="top:258px"><svg width="14" height="18" viewBox="0 0 14 18"><path d="M7 1a6 6 0 0 0-6 6c0 4.5 6 10 6 10s6-5.5 6-10a6 6 0 0 0-6-6z" fill="none" stroke="#3fb3f2" stroke-width="1.6"/><circle cx="7" cy="7" r="2" fill="#3fb3f2"/></svg>Area Name<svg class="chev" width="8" height="12" viewBox="0 0 8 12"><path d="M2 2l4 4-4 4" fill="none" stroke="rgba(160,200,240,.6)" stroke-width="1.4"/></svg></div>
  <div class="area-sep" style="top:286px"></div>
  <div class="area" style="top:304px"><svg width="14" height="18" viewBox="0 0 14 18"><path d="M7 1a6 6 0 0 0-6 6c0 4.5 6 10 6 10s6-5.5 6-10a6 6 0 0 0-6-6z" fill="none" stroke="#3fb3f2" stroke-width="1.6"/><circle cx="7" cy="7" r="2" fill="#3fb3f2"/></svg>Area Name<svg class="chev" width="8" height="12" viewBox="0 0 8 12"><path d="M2 2l4 4-4 4" fill="none" stroke="rgba(160,200,240,.6)" stroke-width="1.4"/></svg></div>
</div>

<svg class="abs" style="left:0;top:2560px" width="1200" height="141" viewBox="0 2560 1200 141">
  <path d="M0 2585 C250 2655 560 2690 820 2684 C980 2680 1110 2650 1200 2600 L1200 2701 L0 2701 Z" fill="#fff"/>
</svg>

<h2 class="abs sec-title" style="left:0;top:2706px;width:1200px;text-align:center;font-size:33px;color:var(--primary)">Testimonials</h2>
<p class="abs" style="left:0;top:2755px;width:1200px;text-align:center;font-size:13px;color:var(--bright)">What Our Client Say About THE SUDSY HARBOR</p>
<svg class="abs" style="left:114px;top:2883px" width="16" height="28" viewBox="0 0 16 28"><path d="M13 2 3 14l10 12" fill="none" stroke="#0054AA" stroke-width="2"/></svg>
<svg class="abs" style="left:1070px;top:2883px" width="16" height="28" viewBox="0 0 16 28"><path d="M3 2l10 12-10 12" fill="none" stroke="#0054AA" stroke-width="2"/></svg>

<div class="testi" style="left:170px;top:2813px">
  <div class="avatar" role="img" aria-label="Client portrait"><span class="q">“</span></div>
  <p>" Lorem Ipsum has been the industry's standard dummy text ever since the 1500s, when an unknown printer took a galley of type and scrambled this"</p>
  <div class="who">—&nbsp;&nbsp; Client Name</div>
</div>
<div class="testi" style="left:470px;top:2813px">
  <div class="avatar" role="img" aria-label="Client portrait" style="background:radial-gradient(circle at 50% 45%,#c98b6a,#4a2a1c)"><span class="q">“</span></div>
  <p>" Lorem Ipsum has been the industry's standard dummy text ever since the 1500s, when an unknown printer took a galley of type and scrambled this"</p>
  <div class="who">—&nbsp;&nbsp; Client Name</div>
</div>
<div class="testi" style="left:770px;top:2813px">
  <div class="avatar" role="img" aria-label="Client portrait" style="background:radial-gradient(circle at 50% 45%,#e7b9a0,#5a2e22)"><span class="q">“</span></div>
  <p>" Lorem Ipsum has been the industry's standard dummy text ever since the 1500s, when an unknown printer took a galley of type and scrambled this"</p>
  <div class="who">—&nbsp;&nbsp; Client Name</div>
</div>

<svg class="abs" style="left:0;top:3100px" width="1200" height="62" viewBox="0 3100 1200 62">
  <path d="M0 3145 C150 3100 320 3110 520 3140 C760 3170 980 3110 1200 3110 L1200 3162 L0 3162 Z" fill="#a9d6f2"/>
  <path d="M0 3158 C180 3125 360 3150 560 3160 C780 3170 980 3118 1200 3125 L1200 3162 L0 3162 Z" fill="#0A1F48"/>
</svg>
<footer class="abs footer"></footer>
<svg class="abs" style="left:209px;top:3224px" width="56" height="52" viewBox="0 0 56 52"><rect x="2" y="6" width="40" height="30" rx="3" fill="none" stroke="#17A2E6" stroke-width="2"/><path d="M2 8l20 16 20-16" fill="none" stroke="#17A2E6" stroke-width="2"/><circle cx="42" cy="36" r="11" fill="#0A1F48" stroke="#17A2E6" stroke-width="2"/><path d="M37 36h9M43 32l4 4-4 4" fill="none" stroke="#17A2E6" stroke-width="2"/></svg>
<div class="abs cta-text">Please Feel Free to Call or Email<br>Us For More Information</div>
<div class="btn" style="left:676px;top:3234px;width:103px;height:41px">Contact Us</div>
<div class="abs rule"></div>

<div class="abs brand" style="left:68px;top:3402px"><span class="dot"></span><span class="name" style="font-size:34px">SUDSY HARBOR</span></div>
<div class="social" style="left:111px;top:3479px"></div>
<div class="social" style="left:162px;top:3479px"></div>
<div class="social" style="left:213px;top:3479px"></div>

<div class="abs col-title" style="left:337px;top:3364px">Sitemap</div>
<ul class="abs links" style="left:337px;top:3402px">
  <li>Home</li><li>About Us</li><li>Services</li><li>Locations</li><li>Reviews</li><li>Contact us</li>
</ul>
<div class="abs col-title" style="left:611px;top:3364px">Services</div>
<ul class="abs links" style="left:611px;top:3402px">
  <li>Dry Cleaning Drop Off</li><li>Professional Laundry</li><li>Wash Dry Fold</li><li>Self Service Laundry</li>
</ul>
<div class="abs col-title" style="left:887px;top:3364px">Contact Us</div>
<div class="icon-badge" style="left:886px;top:3401px"><svg width="14" height="18" viewBox="0 0 14 18"><path d="M7 1a6 6 0 0 0-6 6c0 4.5 6 10 6 10s6-5.5 6-10a6 6 0 0 0-6-6z" fill="none" stroke="#fff" stroke-width="1.8"/><circle cx="7" cy="7" r="2" fill="#fff"/></svg></div>
<p class="abs" style="left:938px;top:3408px;width:190px;font-size:11px;line-height:19px;color:#fff">Harborview Plaza, 210 Linden Ave NE, # 12, Riverton, GA 30308</p>
<div class="icon-badge" style="left:886px;top:3473px"><svg width="18" height="18" viewBox="0 0 24 24"><path d="M6.6 10.8a15 15 0 0 0 6.6 6.6l2.2-2.2a1 1 0 0 1 1-.25 11.4 11.4 0 0 0 3.6.57 1 1 0 0 1 1 1V20a1 1 0 0 1-1 1A17 17 0 0 1 3 4a1 1 0 0 1 1-1h3.5a1 1 0 0 1 1 1c0 1.25.2 2.45.57 3.57a1 1 0 0 1-.25 1z" fill="#fff"/></svg></div>
<div class="abs" style="left:938px;top:3480px;font-size:18px;font-weight:500;color:#fff">(404) 555-0182</div>
<div class="abs" style="left:941px;top:3511px;font-size:14px;color:#fff">Delivery Available</div>

<div class="abs copyright">©THE SUDSY HARBOR &nbsp;- 2021 All rights reserved.</div>

</body>
</html>
```